Premium Food Label Design – High-End Boutique Jar Labels (3 Sizes)

I require a complete jar label redesign across three sizes:
75mm x 130mm (Large & Medium)
55mm x 120mm (Small)
45mm x 120mm (XS)

The design must feel professional, modern, elegant, and high-end boutique.
Primary aesthetic: white, minimal, refined, with accents in soft brown and gold/bronze. (see prefer colours of logo in OLD LABEL PDF)
Transparent background required.

I have attached my current label for wording reference only — I want to move away from the kraft look entirely.
The label must include all existing details, plus a dedicated space to manually add batch number and date.

IMPORTANT: Final files must be supplied as editable Adobe Illustrator (.AI) files with live text layers (not outlined) so I can update them as needed.
Logo is attached. I’m open to a fresh, elevated design direction aligned with a premium brand feel.
Updates

Low design quality

Target Market(s)

People who appreciate high-end, thoughtfully crafted food and are willing to pay for quality

Industry/Entity Type

Gourmet Food / Artisan Food Packaging

Requirements
Must have
• Premium, minimal aesthetic, Strong typography hierarchy, White background, Consistency across 3 sizes
Nice to have
• Elevated “Amber Meadow” styling
Should not have
• No bright or bold colours, No clutter or overcrowding, No heavy borders or thick frames,No “homemade/craft” fonts

```html
<!DOCTYPE html>
<html lang="en">
<head>
<meta charset="utf-8">
<title>Kindred Table Tomato Relish – Jar Labels</title>
<link href="https://fonts.googleapis.com/css2?family=Montserrat:wght@400;500;600;700;800;900&display=swap" rel="stylesheet">
<style>
  :root {
    --canvas: #efefed;
    --label: #fbfbfa;
    --olive: #8a9462;
    --olive-deep: #6e8c35;
    --leaf: #7f9a45;
    --brown: #6b5a4e;
    --brown-dark: #5a4038;
    --grey: #8e8e8e;
    --grey-light: #a3a3a3;
    --rule: #b9b9b9;
    --ink: #2f2f2f;
    --tomato: #a8321e;
    --tomato-deep: #6e1e10;
  }
  * { margin: 0; padding: 0; box-sizing: border-box; }
  html, body {
    width: 1200px;
    height: 4129px;
    overflow: hidden;
    background: var(--canvas);
    font-family: "Montserrat", sans-serif;
  }
  .canvas { position: relative; width: 1200px; height: 4129px; }

  .label {
    position: absolute;
    background: var(--label);
    border-radius: 60px;
    box-shadow: 0 6px 30px rgba(0,0,0,0.08);
    overflow: hidden;
  }
  .label--front { left: 208px; top: 533px; width: 842px; height: 1000px; }
  .label--front svg { display: block; }

  .label--back { left: 99px; top: 2620px; width: 938px; height: 1097px; }
  .back-title {
    position: absolute; left: 0; right: 0; top: 62px;
    text-align: center; font-weight: 800; font-size: 58px;
    color: var(--grey); letter-spacing: 1px;
  }
  .back-intention {
    position: absolute; left: 100px; right: 100px; top: 146px;
    text-align: center; font-weight: 500; font-size: 18px;
    line-height: 23px; color: var(--grey-light); text-transform: uppercase;
  }
  .back-heading {
    position: absolute; left: 0; right: 0; top: 244px;
    text-align: center; font-weight: 800; font-size: 44px;
    color: var(--olive-deep);
  }
  .ingredients {
    position: absolute; left: 152px; width: 634px; top: 316px;
    border-top: 2px dashed var(--rule);
    list-style: none;
  }
  .ingredients li {
    display: flex; justify-content: space-between; align-items: flex-end;
    height: 50.7px; padding-bottom: 2px;
    border-bottom: 1.5px solid var(--rule);
    font-size: 26px; font-weight: 500; color: var(--grey-light);
    text-transform: uppercase;
  }
  .ingredients li:first-child { height: 64px; }
  .ingredients .qty { color: var(--grey); }

  .maker {
    position: absolute; left: 62px; top: 776px;
    font-size: 20px; font-weight: 600; line-height: 24px;
    color: var(--ink); text-transform: uppercase;
  }
  .storage {
    position: absolute; left: 493px; top: 800px;
    font-size: 20px; font-weight: 600; line-height: 24px;
    color: var(--ink); text-transform: uppercase;
  }
  .batch {
    position: absolute; left: 62px; top: 942px;
    font-size: 17px; font-weight: 600; color: var(--ink);
  }
  .batch span {
    display: inline-block; width: 96px; border-bottom: 1.5px solid var(--ink);
    margin-right: 8px;
  }
  .batch span.short { width: 92px; margin-right: 0; }
  .batch-box {
    position: absolute; left: 494px; top: 902px; width: 377px; height: 136px;
    border: 1.5px solid var(--grey); border-radius: 14px;
  }
</style>
</head>
<body>
<main class="canvas">

  <section class="label label--front" aria-label="Front label">
    <svg width="842" height="1000" viewBox="0 0 842 1000" xmlns="http://www.w3.org/2000/svg">
      <defs>
        <linearGradient id="illustration-tone" x1="0" y1="0" x2="0.3" y2="1">
          <stop offset="0" stop-color="#6f8f3a"/>
          <stop offset="0.3" stop-color="#a8321e"/>
          <stop offset="1" stop-color="#6e1e10"/>
        </linearGradient>
      </defs>

      <rect class="hero-illustration" x="430" y="152" width="390" height="528" rx="40"
            fill="url(#illustration-tone)" opacity="0.9"
            role="img" aria-label="Illustration of a ripe tomato with sprouting green leaves"/>

      <text class="product-name" transform="translate(176 915) rotate(-90)"
            font-family="Montserrat, sans-serif" font-weight="900" font-size="200"
            fill="var(--olive)" textLength="856" lengthAdjust="spacingAndGlyphs">TOMATO</text>

      <text class="product-type" transform="translate(264 915) rotate(-90)"
            font-family="Montserrat, sans-serif" font-weight="500" font-size="70"
            fill="var(--brown)" textLength="432" lengthAdjust="spacing">RELISH</text>

      <line class="divider" x1="237" y1="235" x2="237" y2="470" stroke="var(--grey-light)" stroke-width="2"/>

      <text class="brand-vertical" transform="translate(366 923) rotate(-90)"
            font-family="Montserrat, sans-serif" font-weight="800" font-size="52"
            fill="var(--grey)" textLength="232" lengthAdjust="spacingAndGlyphs">KINDRED</text>
      <rect class="brand-tag" x="376" y="691" width="32" height="232" fill="var(--leaf)"/>
      <text transform="translate(401 918) rotate(-90)"
            font-family="Montserrat, sans-serif" font-weight="600" font-size="24"
            fill="#ffffff" textLength="220" lengthAdjust="spacing">TABLE</text>

      <g class="brand-name" font-family="Montserrat, sans-serif" font-weight="400" fill="var(--brown-dark)" text-anchor="middle">
        <text x="445" y="98" font-size="52" letter-spacing="2">KINDRED</text>
        <text x="445" y="138" font-size="30" letter-spacing="6">TABLE</text>
      </g>

      <circle class="quality-seal" cx="733" cy="808" r="46" fill="#ffffff" stroke="var(--leaf)" stroke-width="4"/>

      <text class="net-weight" x="711" y="915" text-anchor="middle"
            font-family="Montserrat, sans-serif" font-weight="800" font-size="56"
            fill="var(--brown-dark)">375G</text>
    </svg>
  </section>

  <section class="label label--back" aria-label="Back label">
    <h2 class="back-title">AMBER MEADOW</h2>
    <p class="back-intention">What is made with love is felt in return. May this relish nourish<br>more than the meal- bringing comfort, connection<br>and joy to every moment shared.</p>
    <h3 class="back-heading">INGREDIENT</h3>
    <ul class="ingredients">
      <li><span>Tomato,</span><span class="qty">0GM</span></li>
      <li><span>Onion</span><span class="qty">0GM</span></li>
      <li><span>Sugar,</span><span class="qty">0GM</span></li>
      <li><span>Vinegar,</span><span class="qty">0GM</span></li>
      <li><span>Salt,</span><span class="qty">0GM</span></li>
      <li><span>Spices,</span><span class="qty">0GM</span></li>
      <li><span>Thikener ( Cornflower)</span><span class="qty">0GM</span></li>
    </ul>
    <p class="maker">Made by Kindred Table,QLD,<br>Australia<br>W: kindredtable.com<br>E: info@kindredtable.com</p>
    <p class="storage">Storage:<br>Keep refrigerated<br>once opened</p>
    <p class="batch">BATCH#<span></span>DATE <span class="short"></span></p>
    <div class="batch-box"></div>
  </section>

</main>
</body>
</html>
```